Neurological Physiotherapy Business seeks Letter Template

Neurological Physiotherapy Service seeking business card design with chosen logo. We are looking for a card that showcases a premium and professional service that is individualised and intensive.

Text preferably easily to read, in moderately large font size as tend to be targeted towards adults more 50 years old.
Updates

Hi all,

I have just completed the brief. Please let me know if you have further questions.

Thanks
K

Hi everyone,

Thank you so much for your wonderful designs - it has made deciding very difficult, however, I have decided on a design and therefore request that no further designs be submitted.

Thanks again,
K

Target Market(s)

Adults with neurological conditions, and their families. Health professionals, insurance companies and other external health networks and organisations who may be interested in referring or receiving letters.

Industry/Entity Type

Professional Service

Font styles to use
Sans Serif

Requirements
Must have
• - Logo
- Australian Business Number (ABN)
- Address (PO Box)
- Company Website
- Email
- Company Phone Number
- Company Fax Number

```html
<!DOCTYPE html>
<html lang="en">
<head>
<meta charset="utf-8">
<title>Norvale – Business Card</title>
<link rel="stylesheet" href="https://fonts.googleapis.com/css2?family=Roboto:wght@300;400;700&display=swap">
<style>
  :root {
    --bg: #e9e7e3;
    --card: #f2f2f1;
    --ink: #4a4a4a;
    --ink-soft: #6b6b6b;
    --blue: #1b8cc6;
    --teal: #0e7480;
    --green: #2f8f3a;
    --lime: #b5c93c;
    --shadow: rgba(0, 0, 0, 0.12);
  }
  * { box-sizing: border-box; margin: 0; padding: 0; }
  html, body {
    width: 1200px;
    height: 900px;
    overflow: hidden;
    background: var(--bg);
    font-family: "Roboto", sans-serif;
    color: var(--ink);
  }
  .canvas {
    width: 1200px;
    height: 900px;
    display: flex;
    align-items: center;
    justify-content: center;
    gap: 60px;
  }
  .card {
    position: relative;
    width: 520px;
    height: 318px;
    background: var(--card);
    box-shadow: 0 2px 10px var(--shadow);
    overflow: hidden;
  }

  /* Front */
  .card--front {
    display: flex;
    align-items: center;
    justify-content: center;
    gap: 22px;
  }
  .brand-dot {
    width: 70px;
    height: 70px;
    border-radius: 50%;
    background: var(--blue);
  }
  .brand {
    display: flex;
    flex-direction: column;
  }
  .brand__name {
    font-weight: 300;
    font-size: 50px;
    letter-spacing: 4px;
    color: var(--ink);
    line-height: 1;
  }
  .brand__tagline {
    font-weight: 300;
    font-size: 13px;
    color: var(--ink-soft);
    margin-top: 6px;
  }
  .brand__web {
    font-weight: 700;
    font-size: 13px;
    margin-top: 6px;
    text-align: right;
  }
  .web__host { color: var(--teal); }
  .web__tld { color: var(--green); }

  /* Back */
  .card-wash {
    position: absolute;
    top: 0;
    right: 0;
    width: 250px;
    height: 140px;
    background: linear-gradient(120deg, var(--blue) 0%, var(--green) 45%, var(--lime) 100%);
    opacity: 0.85;
    border-bottom-left-radius: 120px 100px;
  }
  .contact {
    position: absolute;
    left: 40px;
    top: 118px;
  }
  .contact__name {
    font-weight: 300;
    font-size: 24px;
    color: var(--ink);
  }
  .contact__role {
    font-size: 11px;
    letter-spacing: 0.5px;
    text-transform: uppercase;
    margin-left: 6px;
    vertical-align: 4px;
  }
  .contact__list {
    list-style: none;
    margin-top: 18px;
    font-weight: 300;
    font-size: 15px;
    line-height: 19px;
  }
  .contact__label {
    display: inline-block;
    width: 22px;
    color: var(--blue);
  }
  .contact__address {
    margin-top: 8px;
    font-weight: 300;
    font-size: 15px;
    line-height: 22px;
  }
  .contact__web {
    margin-top: 10px;
    font-weight: 700;
    font-size: 15px;
  }
</style>
</head>
<body>
<main class="canvas">
  <section class="card card--front" aria-label="Card front">
    <span class="brand-dot"></span>
    <div class="brand">
      <span class="brand__name">NORVALE</span>
      <span class="brand__tagline">intensive neuro therapies</span>
      <span class="brand__web"><span class="web__host">www.norvale</span><span class="web__tld">.com.au</span></span>
    </div>
  </section>

  <section class="card card--back" aria-label="Card back">
    <div class="card-wash" role="img" aria-label="Soft blue to green brand colour wash"></div>
    <div class="contact">
      <p class="contact__name">Daniel Reyes<span class="contact__role">Manager</span></p>
      <ul class="contact__list">
        <li><span class="contact__label">T</span>0400 315 742</li>
        <li><span class="contact__label">F</span>0400 315 748</li>
        <li><span class="contact__label">E</span>daniel.reyes@norvale.com.au</li>
      </ul>
      <p class="contact__address">PO Box 2210 Riverbend NT 0830<br>ABN 987654321</p>
      <p class="contact__web"><span class="web__host">www.norvale</span><span class="web__tld">.com.au</span></p>
    </div>
  </section>
</main>
</body>
</html>
```